Elegant Business Card for Technology Company

Client is a supplier of innovative industrial communications and automation equipment since 2002. This contest is to gather fresh ideas for a redesign of the existing business card. Client is looking for design that best communicates tagline "Industrial Networking and Computing Specialist".

Design submissions should look modern, clean, elegant and professional. It should not be cluttered. Use white as the primary colour. Orange and black as secondary colour. Refer to jpeg File 1 on the current design.

Fonts used by Client used include Arial Regular, Arial Black, Roboto Regular, Roboto Black and Lato.

The winning design will be sent for offset printing using super white 250gsm artcard paper (open for suggestions).

Target Market(s)

System Engineers, Project Managers, Purchasing Managers from companies providing engineering services for Smart Cities.

Industry/Entity Type

Information Technology

Contact Information for Business Card

Refer to PDF File 3 for Business Card Details. Priority of short contact information would be as follows Name > Job Title > Email > Mobile > Web > Tel > Fax > Business Address >UEN (UEN represents company registration number)

Font styles to use
Sans Serif

Colors
ffffff
f37122
000000
5c5c5c

Requirements
Must have
• Refer to AI File 2 (Company Logo) & PDF File 3 (Information on Namecard)
Should not have
• No QR codes
• No Social Media Icons
• Do not create full Black or Orange colour background

```html
<!DOCTYPE html>
<html lang="en">
<head>
<meta charset="utf-8">
<title>NDL Business Card</title>
<link rel="stylesheet" href="https://fonts.googleapis.com/css2?family=Open+Sans:wght@400;600;800&display=swap">
<style>
  :root {
    --white: #ffffff;
    --orange: #f37122;
    --black: #000000;
    --grey: #5c5c5c;
    --backdrop: #8c8c8c;
    --tint: #fdf4ee;
  }
  * { margin: 0; padding: 0; box-sizing: border-box; }
  html, body {
    width: 1105px; height: 1200px; overflow: hidden;
    background: var(--backdrop);
    font-family: "Open Sans", Arial, sans-serif;
  }
  .card {
    position: absolute; left: 198px;
    width: 709px; height: 427px;
    background: var(--white);
    overflow: hidden;
  }
  .card--front { top: 119px; }
  .card--back { top: 635px; }

  .front-wave { position: absolute; left: 0; top: 0; width: 709px; height: 427px; }

  .brand { position: absolute; left: 240px; top: 40px; display: flex; align-items: center; gap: 18px; }
  .brand__dot { width: 120px; height: 120px; border-radius: 50%; background: var(--orange); }
  .brand__name { font-weight: 800; font-size: 96px; line-height: 1; color: var(--black); letter-spacing: 2px; }

  .person {
    position: absolute; left: 50px; right: 50px; top: 255px;
    display: flex; align-items: center; gap: 14px; color: var(--white);
  }
  .person__rule { flex: 1; height: 1.5px; background: var(--white); }
  .person__name { font-weight: 600; font-size: 25px; white-space: nowrap; }
  .person__title { font-size: 18px; white-space: nowrap; }

  .contacts { position: absolute; left: 52px; top: 294px; list-style: none; color: var(--white); font-size: 19px; }
  .contacts li { display: flex; align-items: center; height: 29px; }
  .contacts svg { width: 18px; height: 18px; margin-right: 10px; fill: var(--white); }

  .address { position: absolute; right: 20px; top: 294px; text-align: right; color: var(--white); font-size: 19px; line-height: 29px; }
  .address__web { font-weight: 600; letter-spacing: 1.5px; }

  .back-field { position: absolute; inset: 0; background: var(--tint); }
  .back-mark {
    position: absolute; left: 298px; top: 83px; width: 166px; height: 166px; border-radius: 50%;
    background: var(--orange); display: flex; align-items: center; justify-content: center;
  }
  .back-mark__name { font-weight: 800; font-size: 48px; color: var(--white); letter-spacing: 2px; }
  .tagline {
    position: absolute; left: 0; right: 0; top: 290px; text-align: center;
    font-size: 20px; line-height: 26.5px; color: var(--black);
  }
</style>
</head>
<body>
  <section class="card card--front">
    <svg class="front-wave" viewBox="0 0 709 427" aria-hidden="true">
      <path d="M0 203 C 200 240, 450 240, 709 202 L709 427 L0 427 Z" fill="var(--orange)"/>
      <path d="M0 184 C 180 220, 420 232, 700 204 C 430 228, 190 222, 0 201 Z" fill="var(--black)"/>
    </svg>

    <div class="brand">
      <span class="brand__dot"></span>
      <span class="brand__name">NDL</span>
    </div>

    <div class="person">
      <span class="person__rule"></span>
      <span class="person__name">Daniel Koh -</span>
      <span class="person__title">Sales Manager</span>
      <span class="person__rule"></span>
    </div>

    <ul class="contacts">
      <li><svg viewBox="0 0 24 24"><path d="M6.6 10.8a15 15 0 0 0 6.6 6.6l2.2-2.2c.3-.3.7-.4 1-.2 1.1.4 2.3.6 3.6.6.6 0 1 .4 1 1V20c0 .6-.4 1-1 1C10.6 21 3 13.4 3 4c0-.6.4-1 1-1h3.5c.6 0 1 .4 1 1 0 1.3.2 2.5.6 3.6.1.3 0 .7-.2 1z"/></svg>+65 6123 4501</li>
      <li><svg viewBox="0 0 24 24"><path d="M7 1h10a2 2 0 0 1 2 2v18a2 2 0 0 1-2 2H7a2 2 0 0 1-2-2V3a2 2 0 0 1 2-2zm0 3v14h10V4z"/></svg>+65 9123 4567</li>
      <li><svg viewBox="0 0 24 24"><path d="M7 2h10v5H7zM3 8h18a1 1 0 0 1 1 1v8h-4v-3H6v3H2V9a1 1 0 0 1 1-1zm4 8h10v6H7z"/></svg>+65 6123 4502</li>
      <li><svg viewBox="0 0 24 24"><path d="M2 5h20v14H2zm2 2v.4l8 5.2 8-5.2V7z"/></svg>sales@ndl.com.sg</li>
    </ul>

    <address class="address">
      22 Kallang Way Lane<br>
      Kallang Hub #05-12 (Lobby B)<br>
      Singapore 349321<br>
      <span class="address__web">www.ndl.com.sg</span>
    </address>
  </section>

  <section class="card card--back">
    <div class="back-field" role="img" aria-label="Faint pale orange dot pattern background"></div>
    <div class="back-mark"><span class="back-mark__name">NDL</span></div>
    <p class="tagline">
      Industrial Networking &amp; Computing Specialist<br>
      Industrial Ethernet / Wireless / Cellular<br>
      Industrial &amp; Embedded Computing / Serial / Fieldbus Connectivity<br>
      IP Video Surveillance / Remote Automation
    </p>
  </section>
</body>
</html>
```